Wealth management firm needs a business card design

Using my logo, create a business card that covers all of the regulatory wordings that I need. It must have - Registered Office 5-7 Pellinore Court, Edinburgh, EH9 2QW. Registered in Scotland under number SC738204. Corvell Wealth Management Ltd is an appointed representative of Quintor wealth management Ltd, which is authorised and regulated by the Monetary Standards Council.

Target Market(s)

professional clients

Industry/Entity Type

finance

Contact Information for Business Card

Corvell Wealth Management, Rupert Ashdown-Kerr, Director, 9 Tanner Row, Edinburgh, EH2 4NP. 07812 455 193, rupert.ashdown-kerr@corvellwealth.example , www.corvellwealth.example

Font styles to use
Serif

Colors
0054AA
0677BA
7BADD7
CADEEF
E8F1F8

Requirements
Must have
• regulatory wording in small text at bottom

```html
<!DOCTYPE html>
<html lang="en">
<head>
<meta charset="utf-8">
<title>Corvell Wealth Management – Business Card</title>
<link rel="stylesheet" href="https://fonts.googleapis.com/css2?family=Sorts+Mill+Goudy:ital@0;1&family=Arimo:wght@400;700&display=swap">
<style>
  :root {
    --card-blue: #1372e0;
    --logo-blue: #7badd7;
    --logo-dot: #2b7fe6;
    --ink-dark: #1c1f2e;
    --paper: #f7f8fa;
    --white: #ffffff;
    --stage: #e8f1f8;
    --serif: "Sorts Mill Goudy", Georgia, serif;
    --sans: "Arimo", Arial, sans-serif;
  }
  * { box-sizing: border-box; margin: 0; padding: 0; }
  html, body { width: 1200px; height: 779px; overflow: hidden; }
  body {
    background: var(--stage);
    display: flex;
    align-items: center;
    justify-content: center;
    gap: 30px;
  }
  .card {
    position: relative;
    width: 560px;
    height: 350px;
    border-radius: 22px;
    overflow: hidden;
    box-shadow: 0 8px 24px rgba(0, 40, 90, .18);
  }

  /* Back: regulatory side */
  .card-back {
    background: var(--card-blue);
    color: var(--white);
    font-family: var(--serif);
    text-align: center;
    padding-top: 62px;
  }
  .brand-mark {
    display: block;
    width: 64px;
    height: 64px;
    margin: 0 auto 10px;
    border-radius: 50%;
    background: var(--logo-blue);
    opacity: .85;
  }
  .card-back .brand-name {
    font-size: 31px;
    color: var(--logo-blue);
    letter-spacing: .5px;
    line-height: 1.1;
  }
  .card-back .brand-tagline {
    font-size: 11px;
    color: var(--logo-blue);
    margin-top: 2px;
    margin-bottom: 20px;
  }
  .regulatory {
    font-size: 13px;
    font-weight: 700;
    line-height: 1.3;
    padding: 0 50px;
  }
  .registration {
    font-size: 12px;
    line-height: 1.35;
    margin-top: 8px;
  }
  .registration em { font-style: italic; }

  /* Front: contact side */
  .card-front { background: var(--paper); }
  .card-front .sweep {
    position: absolute;
    inset: 0;
    width: 100%;
    height: 100%;
  }
  .sweep .edge { fill: var(--ink-dark); }
  .sweep .panel { fill: var(--card-blue); }

  .front-brand {
    position: absolute;
    left: 14px;
    top: 128px;
    width: 250px;
    text-align: center;
    font-family: var(--serif);
    color: var(--ink-dark);
  }
  .front-brand .brand-mark {
    width: 40px;
    height: 40px;
    margin-bottom: 8px;
    background: var(--logo-dot);
    opacity: 1;
  }
  .front-brand .brand-name { font-size: 17px; line-height: 1.15; }
  .front-brand .brand-tagline { font-size: 8px; margin-top: 2px; }

  .contact {
    position: absolute;
    right: 26px;
    top: 40px;
    text-align: right;
    color: var(--white);
    font-family: var(--sans);
  }
  .contact .person {
    font-family: var(--serif);
    font-weight: 700;
    font-size: 22px;
    letter-spacing: .3px;
  }
  .contact .role { font-size: 12px; margin-top: 1px; }
  .contact address {
    font-style: normal;
    font-size: 13px;
    line-height: 1.25;
    margin-top: 42px;
  }
  .contact-list {
    list-style: none;
    margin-top: 34px;
    font-size: 12px;
    line-height: 1.45;
  }
  .contact-list li {
    display: flex;
    align-items: center;
    justify-content: flex-end;
    gap: 7px;
  }
  .contact-list svg { width: 11px; height: 11px; fill: var(--white); flex: none; }
</style>
</head>
<body>

  <section class="card card-back" aria-label="Business card, regulatory side">
    <span class="brand-mark" aria-hidden="true"></span>
    <div class="brand-name">Corvell Wealth Management Ltd</div>
    <div class="brand-tagline">Personal Financial Advice</div>
    <p class="regulatory">Corvell Wealth Management Ltd is an appointed representative of Quintor wealth management Ltd, which is authorised and regulated by the Monetary Standards Council.</p>
    <p class="registration"><em>Registered Office</em> 5-7 Pellinore Court, Edinburgh, EH9 2QW.<br><em>Registered</em> in Scotland under number SC738204.</p>
  </section>

  <section class="card card-front" aria-label="Business card, contact side">
    <svg class="sweep" viewBox="0 0 560 350" preserveAspectRatio="none" aria-hidden="true">
      <path class="edge" d="M138 0 C255 28 302 160 246 350 L560 350 L560 0 Z"/>
      <path class="panel" d="M150 0 C262 30 312 160 252 350 L560 350 L560 0 Z"/>
    </svg>

    <div class="front-brand">
      <span class="brand-mark" aria-hidden="true"></span>
      <div class="brand-name">Corvell Wealth Management Ltd</div>
      <div class="brand-tagline">Personal Financial Advice</div>
    </div>

    <div class="contact">
      <div class="person">Rupert Ashdown-Kerr</div>
      <div class="role">Director</div>
      <address>9 Tanner Row<br>Edinburgh<br>EH2 4NP.</address>
      <ul class="contact-list">
        <li>07812 455 193
          <svg viewBox="0 0 24 24" aria-hidden="true"><path d="M6.6 10.8a15.1 15.1 0 0 0 6.6 6.6l2.2-2.2a1 1 0 0 1 1-.25 11.4 11.4 0 0 0 3.6.57 1 1 0 0 1 1 1V20a1 1 0 0 1-1 1A17 17 0 0 1 3 4a1 1 0 0 1 1-1h3.5a1 1 0 0 1 1 1c0 1.25.2 2.45.57 3.6a1 1 0 0 1-.25 1z"/></svg>
        </li>
        <li>rupert.ashdown-kerr@corvellwealth.example
          <svg viewBox="0 0 24 24" aria-hidden="true"><path d="M2 5h20v14H2z M4 7v.5l8 5 8-5V7l-8 5z" fill-rule="evenodd"/></svg>
        </li>
        <li>www.corvellwealth.example
          <svg viewBox="0 0 24 24" aria-hidden="true"><path d="M12 2a10 10 0 1 0 0 20 10 10 0 0 0 0-20zm0 2c1.2 1.4 2 3.5 2.2 6H9.8C10 7.5 10.8 5.4 12 4zm-2.2 8h4.4c-.2 2.5-1 4.6-2.2 6-1.2-1.4-2-3.5-2.2-6zM4.1 12h3.7c.1 2.2.7 4.2 1.6 5.7A8 8 0 0 1 4.1 12zm0-2a8 8 0 0 1 5.3-5.7C8.5 5.8 7.9 7.8 7.8 10zm12.1 2h3.7a8 8 0 0 1-5.3 5.7c.9-1.5 1.5-3.5 1.6-5.7zm0-2c-.1-2.2-.7-4.2-1.6-5.7A8 8 0 0 1 19.9 10z"/></svg>
        </li>
      </ul>
    </div>
  </section>

</body>
</html>
```